I need bigcommerce design template

hi, am looking for a quality, professional, attractive and mature bigcommerce template for my site. My site will sell clothes and bags and shoes. Basically what you are to do is setup the store. I have domain name which hostwren will attach them self.

```html
<!DOCTYPE html>
<html lang="en">
<head>
<meta charset="utf-8">
<title>Velvet Lane — Store</title>
<link rel="stylesheet" href="https://fonts.googleapis.com/css2?family=Oswald:wght@400;500;700&family=Arimo:wght@400;700&display=swap">
<style>
:root{
  --red:#d7141a;
  --red-dark:#9c0f12;
  --red-deep:#6e0a0c;
  --orange:#f07a2a;
  --ink:#222;
  --muted:#666;
  --line:#e2e2e2;
  --white:#fff;
  --slate:#2f4450;
}
*{box-sizing:border-box;margin:0;padding:0}
html,body{width:693px;height:1200px;overflow:hidden;background:var(--white)}
body{position:relative;font-family:"Arimo",Arial,sans-serif;color:var(--ink)}
.abs{position:absolute}

/* header */
.brand{left:131px;top:12px;font-family:"Oswald",sans-serif;font-weight:700;font-size:15px;letter-spacing:.5px;color:var(--orange);text-transform:uppercase}
.account-links{right:138px;top:12px;display:flex;gap:14px;font-size:5px;color:var(--red);text-transform:uppercase}
.search{right:138px;top:21px;width:89px;height:9px;border:1px solid var(--line);font-size:4.5px;color:var(--red);text-align:right;padding:2px 3px;text-transform:uppercase}

.main-nav{left:0;top:42px;width:693px;height:15px;background:var(--red-dark);border-bottom:2px solid var(--orange)}
.main-nav ul{position:absolute;left:335px;top:0;display:flex;list-style:none;font-size:6px;color:var(--white)}
.main-nav li{height:13px;line-height:13px;padding:0 8px}
.main-nav li.active{background:var(--red-deep);color:var(--orange)}

/* hero */
.hero{left:0;top:58px;width:693px;height:239px;overflow:hidden;background:radial-gradient(ellipse at 65% 55%,#d21a1a 0%,#8d0c0c 40%,#3a0505 80%,#1a0202 100%)}
.hero-title{left:168px;top:111px;font-family:"Oswald",sans-serif;font-weight:500;font-size:14px;line-height:17px;color:var(--white);text-transform:uppercase}
.hero-arrow{top:112px}
.hero-dots{left:136px;top:223px;display:flex;gap:3px}
.hero-dots span{width:6px;height:6px;background:var(--white)}
.hero-dots span.on{background:var(--orange)}

/* welcome */
.welcome{left:0;top:298px;width:693px;height:160px;background:linear-gradient(160deg,#3d5663,#22323b 60%,#2f4450)}
.welcome-card{left:135px;top:10px;width:421px;height:137px;background:var(--white)}
.welcome-photo{left:8px;top:8px;width:197px;height:123px;background:linear-gradient(135deg,#9aa3a8,#e6e9ea 50%,#6b7378)}
.welcome-title{left:16px;top:24px;font-family:"Oswald",sans-serif;font-size:10px;line-height:12px;color:var(--white);text-transform:uppercase}
.welcome-text{left:215px;top:30px;width:198px;font-size:6.4px;line-height:8.5px;color:#333;text-align:justify}
.welcome-text p+p{margin-top:8px}
.btn{background:var(--red);color:var(--white);font-family:"Oswald",sans-serif;font-size:7.5px;text-align:center}
.read-more{left:363px;top:113px;width:50px;height:18px;line-height:18px}

/* new arrivals */
.section-tab{left:0;top:459px;width:232px;height:17px}
.section-tab span{position:absolute;left:142px;top:0;line-height:17px;font-family:"Oswald",sans-serif;font-size:9.5px;color:var(--white);text-transform:uppercase}

.product{width:122px;height:217px;background:var(--white);box-shadow:0 0 3px rgba(0,0,0,.25)}
.product-photo{position:absolute;left:7px;top:7px;width:109px;height:147px}
.photo-orange{background:linear-gradient(160deg,#c9c9c9,#e8894a 50%,#b7b7b7)}
.photo-violet{background:linear-gradient(160deg,#f4f4f4,#7b3fc4 55%,#e9e9e9)}
.photo-sepia{background:linear-gradient(160deg,#5d4a3a,#a99a84 55%,#3e3128)}
.product-name{position:absolute;left:7px;top:161px;font-size:4.6px;font-weight:700;text-transform:uppercase}
.product-desc{position:absolute;left:7px;top:168px;font-size:3.8px;color:#444;text-transform:uppercase}
.product-icons{position:absolute;right:7px;top:157px}
.product-price{position:absolute;left:7px;top:181px;width:109px;display:flex;justify-content:space-between;font-family:"Oswald",sans-serif;font-size:6.6px;color:var(--red);letter-spacing:.3px}
.buy{position:absolute;left:46px;top:197px;width:30px;height:10px;line-height:10px;font-size:5px}

.load-more{left:299px;top:968px;width:84px;height:22px;display:flex;align-items:center;justify-content:center;gap:6px;font-size:10px}

/* footer */
.newsletter{left:0;top:1008px;width:693px;height:23px;background:linear-gradient(var(--red),var(--red-dark))}
.newsletter-label{left:131px;top:0;line-height:23px;font-family:"Oswald",sans-serif;font-size:6.5px;color:var(--white);letter-spacing:.4px}
.newsletter-field{left:174px;top:4px;width:263px;height:15px;background:var(--white)}
.subscribe{left:447px;top:0;line-height:23px;font-family:"Oswald",sans-serif;font-size:6.5px;color:var(--white);letter-spacing:.4px}
.social{left:516px;top:8px;display:flex;gap:6px}
.social span{width:6px;height:6px;border-radius:50%;background:var(--red-deep)}

.footer-col{top:1043px}
.footer-col h3{font-family:"Oswald",sans-serif;font-weight:400;font-size:8px;color:#333;text-transform:uppercase;padding-bottom:6px;border-bottom:1px solid var(--line);width:90px;margin-bottom:8px}
.footer-col ul{list-style:none;font-size:5.4px;color:#555;line-height:11px}
.store-item{display:flex;gap:8px;font-size:5.4px;color:#555;line-height:9px;margin-bottom:8px}
.store-item svg{flex:none}

.copyright{left:0;top:1161px;width:693px;height:39px;background:linear-gradient(var(--red),var(--red-dark))}
.copyright span{position:absolute;left:145px;top:7px;font-size:5.5px;color:var(--white)}
</style>
</head>
<body>

<header>
  <div class="abs brand">Velvet Lane</div>
  <div class="abs account-links"><span>Sign in | Sign up</span><span>My account</span><span>My cart</span></div>
  <div class="abs search">Search</div>
  <nav class="abs main-nav">
    <ul>
      <li class="active">Home</li><li>About</li><li>Online Shopping</li><li>What's New</li><li>Faq</li><li>Contact</li>
    </ul>
  </nav>
</header>

<section class="abs hero" role="img" aria-label="Model in a flowing red gown against billowing red fabric">
  <div class="abs hero-title">Lorem ipsum dolor sit amet conse<br>ctetur adipisicing elit</div>
  <svg class="abs hero-arrow" style="left:132px" width="22" height="26" viewBox="0 0 22 26"><path d="M18 2 6 13l12 11" fill="none" stroke="#fff" stroke-opacity=".6" stroke-width="5"/></svg>
  <svg class="abs hero-arrow" style="left:533px" width="22" height="26" viewBox="0 0 22 26"><path d="M4 2l12 11L4 24" fill="none" stroke="#fff" stroke-opacity=".6" stroke-width="5"/></svg>
  <div class="abs hero-dots"><span class="on"></span><span></span><span></span><span></span></div>
</section>

<section class="abs welcome">
  <div class="abs welcome-card">
    <div class="abs welcome-photo" role="img" aria-label="Model in a flowing white gown">
      <div class="abs welcome-title">Welcome to<br>Velvet Lane</div>
    </div>
    <div class="abs welcome-text">
      <p>Lorem ipsum dolor sit amet, consectetur adipiscing elit. Nullam viverra odio id tristique condimentum. Aliquam erat volutpat. Morbi ultrices accumsan dui, et venenatis mauris finibus quis. Lorem ipsum dolor sit amet, consectetur adipiscing elit. Nullam viverra odio id tristique condimentum.</p>
      <p>Aliquam erat volutpat. Morbi ultrices accumsan dui, et venenatis mauris finibus quis.</p>
    </div>
    <div class="abs btn read-more">Read More</div>
  </div>
</section>

<div class="abs section-tab">
  <svg width="232" height="17" viewBox="0 0 232 17"><polygon points="0,0 232,0 218,17 0,17" fill="#d7141a"/></svg>
  <span>New Arrivals</span>
</div>

<main>
  <!-- row 1 -->
  <article class="abs product" style="left:135px;top:493px">
    <div class="product-photo photo-orange" role="img" aria-label="Model in an orange flowing dress"></div>
    <div class="product-icons"><svg width="20" height="7" viewBox="0 0 20 7"><path d="M1 4l2 2 4-5" fill="none" stroke="#8ab06a" stroke-width="1"/><path d="M15 6.5 12 3.5a1.6 1.6 0 0 1 3-1.8 1.6 1.6 0 0 1 3 1.8z" fill="none" stroke="#999" stroke-width=".8"/></svg></div>
    <div class="product-name">Lorem ipsumt</div>
    <div class="product-desc">Ex malesuada a justo et mattis, ex malesuada</div>
    <div class="product-price"><span>$199.00AFTER</span><span>CODE: $159.20</span></div>
    <div class="btn buy">BUY</div>
  </article>
  <article class="abs product" style="left:280px;top:493px">
    <div class="product-photo photo-violet" role="img" aria-label="Model in a purple satin gown"></div>
    <div class="product-icons"><svg width="20" height="7" viewBox="0 0 20 7"><path d="M1 4l2 2 4-5" fill="none" stroke="#8ab06a" stroke-width="1"/><path d="M15 6.5 12 3.5a1.6 1.6 0 0 1 3-1.8 1.6 1.6 0 0 1 3 1.8z" fill="none" stroke="#999" stroke-width=".8"/></svg></div>
    <div class="product-name">Lorem ipsumt</div>
    <div class="product-desc">Ex malesuada a justo et mattis, ex malesuada</div>
    <div class="product-price"><span>$199.00AFTER</span><span>CODE: $159.20</span></div>
    <div class="btn buy">BUY</div>
  </article>
  <article class="abs product" style="left:425px;top:493px">
    <div class="product-photo photo-sepia" role="img" aria-label="Model in a short white dress"></div>
    <div class="product-icons"><svg width="20" height="7" viewBox="0 0 20 7"><path d="M1 4l2 2 4-5" fill="none" stroke="#8ab06a" stroke-width="1"/><path d="M15 6.5 12 3.5a1.6 1.6 0 0 1 3-1.8 1.6 1.6 0 0 1 3 1.8z" fill="none" stroke="#999" stroke-width=".8"/></svg></div>
    <div class="product-name">Lorem ipsumt</div>
    <div class="product-desc">Ex malesuada a justo et mattis, ex malesuada</div>
    <div class="product-price"><span>$199.00AFTER</span><span>CODE: $159.20</span></div>
    <div class="btn buy">BUY</div>
  </article>
  <!-- row 2 -->
  <article class="abs product" style="left:135px;top:730px">
    <div class="product-photo photo-orange" role="img" aria-label="Model in an orange flowing dress"></div>
    <div class="product-icons"><svg width="20" height="7" viewBox="0 0 20 7"><path d="M1 4l2 2 4-5" fill="none" stroke="#8ab06a" stroke-width="1"/><path d="M15 6.5 12 3.5a1.6 1.6 0 0 1 3-1.8 1.6 1.6 0 0 1 3 1.8z" fill="none" stroke="#999" stroke-width=".8"/></svg></div>
    <div class="product-name">Lorem ipsumt</div>
    <div class="product-desc">Ex malesuada a justo et mattis, ex malesuada</div>
    <div class="product-price"><span>$199.00AFTER</span><span>CODE: $159.20</span></div>
    <div class="btn buy">BUY</div>
  </article>
  <article class="abs product" style="left:280px;top:730px">
    <div class="product-photo photo-violet" role="img" aria-label="Model in a purple satin gown"></div>
    <div class="product-icons"><svg width="20" height="7" viewBox="0 0 20 7"><path d="M1 4l2 2 4-5" fill="none" stroke="#8ab06a" stroke-width="1"/><path d="M15 6.5 12 3.5a1.6 1.6 0 0 1 3-1.8 1.6 1.6 0 0 1 3 1.8z" fill="none" stroke="#999" stroke-width=".8"/></svg></div>
    <div class="product-name">Lorem ipsumt</div>
    <div class="product-desc">Ex malesuada a justo et mattis, ex malesuada</div>
    <div class="product-price"><span>$199.00AFTER</span><span>CODE: $159.20</span></div>
    <div class="btn buy">BUY</div>
  </article>
  <article class="abs product" style="left:425px;top:730px">
    <div class="product-photo photo-sepia" role="img" aria-label="Model in a short white dress"></div>
    <div class="product-icons"><svg width="20" height="7" viewBox="0 0 20 7"><path d="M1 4l2 2 4-5" fill="none" stroke="#8ab06a" stroke-width="1"/><path d="M15 6.5 12 3.5a1.6 1.6 0 0 1 3-1.8 1.6 1.6 0 0 1 3 1.8z" fill="none" stroke="#999" stroke-width=".8"/></svg></div>
    <div class="product-name">Lorem ipsumt</div>
    <div class="product-desc">Ex malesuada a justo et mattis, ex malesuada</div>
    <div class="product-price"><span>$199.00AFTER</span><span>CODE: $159.20</span></div>
    <div class="btn buy">BUY</div>
  </article>

  <div class="abs btn load-more">
    <svg width="12" height="12" viewBox="0 0 12 12"><circle cx="6" cy="6" r="4.2" fill="none" stroke="#fff" stroke-width="2.2"/></svg>
    <span>LOAD MORE</span>
  </div>
</main>

<footer>
  <div class="abs newsletter">
    <div class="abs newsletter-label">NEWSLETTER</div>
    <div class="abs newsletter-field"></div>
    <div class="abs subscribe">SUBSCRIBE</div>
    <div class="abs social"><span></span><span></span><span></span></div>
  </div>

  <div class="abs footer-col" style="left:136px">
    <h3>Information</h3>
    <ul><li>Specials</li><li>New products</li><li>Top sellers</li><li>Our stores</li><li>Contact us</li><li>Sitemap</li></ul>
  </div>
  <div class="abs footer-col" style="left:237px">
    <h3>My Account</h3>
    <ul><li>My orders</li><li>My merchandise returns</li><li>My credit slips</li><li>My addresses</li><li>My personal info</li></ul>
  </div>
  <div class="abs footer-col" style="left:342px">
    <h3>Store Information</h3>
    <div class="store-item"><svg width="9" height="7" viewBox="0 0 9 7"><rect width="9" height="7" fill="#d7141a"/><path d="M0 0l4.5 3.5L9 0" fill="none" stroke="#fff" stroke-width=".8"/></svg><span>Our Loremipsum dolor</span></div>
    <div class="store-item"><svg width="9" height="9" viewBox="0 0 9 9"><path d="M1 1.5 3 .5l1.3 2.3-1.2.9a5 5 0 0 0 2.2 2.2l.9-1.2L8.5 6l-1 2C4 8 1 5 1 1.5z" fill="#d7141a"/></svg><span>012 345 6789 00</span></div>
    <div class="store-item"><svg width="9" height="11" viewBox="0 0 9 11"><path d="M4.5 11S0 6.5 0 4a4.5 4.5 0 0 1 9 0c0 2.5-4.5 7-4.5 7z" fill="#d7141a"/><circle cx="4.5" cy="4" r="1.6" fill="#fff"/></svg><span>Our Lorem ipsum dolor<br>sit amet, consectetur a<br>dipiscing elit.</span></div>
  </div>

  <div class="abs copyright"><span>© 2015 Velvet Lane</span></div>
</footer>

</body>
</html>
```